FREIGHT FORWARDING FLYER

We need a flyer designed for our company (Brightwater Haulage Global) showing the list of services we offer to hand out to customers. Below is a list of services:<br/><br/>-Ocean/Air Import and Export<br/>-Exhibition Cargo<br/>-Carnet Application<br/>-Project Cargo (OOG/Flatrack/Reefer/DG)<br/>-Customs Clearance<br/>-Door to Door Services<br/>-Cargo Insurance<br/>-Warehousing<br/>-Trucking (LTL/FCL)

Target Market(s)

Customers who have a specific need for freight forwarding, especially customers at exhibitions.

Industry/Entity Type

Freight Forwarding

Colors

Designer to choose colors to be used in the design.

Requirements
Must have
• The services we offer need to pop to the customer and essentially get that interested in the services we offer.

```html
<!DOCTYPE html>
<html lang="en">
<head>
<meta charset="utf-8">
<title>Brightwater Haulage Global – Freight Forwarding Flyer</title>
<link rel="stylesheet" href="https://fonts.googleapis.com/css2?family=Montserrat:ital,wght@0,800;1,800&family=Roboto:ital,wght@0,500;1,400&display=swap">
<style>
  :root {
    --orange: #fc4a05;
    --ink: #1a1816;
    --map-dark: #2e2927;
    --slate: #5b6670;
    --white: #ffffff;
    --paper: #ffffff;
  }
  * { box-sizing: border-box; margin: 0; padding: 0; }
  html, body { width: 927px; height: 1200px; overflow: hidden; background: var(--paper); }
  .flyer { position: relative; width: 927px; height: 1200px; background: var(--paper); font-family: "Roboto", Arial, sans-serif; color: var(--ink); }

  /* Header */
  .brand { position: absolute; left: 28px; top: 46px; display: flex; align-items: center; gap: 14px; }
  .brand-mark { width: 40px; height: 40px; background: var(--orange); }
  .brand-name { font-family: "Roboto", Arial, sans-serif; font-weight: 500; font-size: 30px; letter-spacing: 1px; line-height: 1; color: var(--slate); text-transform: uppercase; }

  .contact-phone { position: absolute; left: 649px; top: 39px; width: 66px; height: 66px; border-radius: 50%; background: var(--orange); display: flex; align-items: center; justify-content: center; }
  .phone-numbers { position: absolute; left: 736px; top: 38px; font-style: italic; font-weight: 400; font-size: 28px; line-height: 36px; color: var(--ink); }

  /* Hero */
  .hero { position: absolute; left: 0; top: 192px; width: 670px; height: 310px; background: var(--orange); box-shadow: 0 4px 8px rgba(0,0,0,.25); overflow: hidden; }
  .hero-map { position: absolute; left: 0; top: 4px; width: 615px; height: 300px; background: radial-gradient(ellipse at 55% 40%, rgba(46,41,39,.55), rgba(46,41,39,.15) 70%, rgba(46,41,39,0) 100%); }
  .hero-title { position: absolute; left: 36px; top: 76px; font-family: "Montserrat", Arial, sans-serif; font-weight: 800; font-size: 50px; line-height: 58px; color: var(--white); text-transform: uppercase; letter-spacing: 1px; }

  /* Photo column */
  .photo-frame { position: absolute; left: 703px; width: 210px; height: 210px; background: var(--orange); box-shadow: 0 4px 8px rgba(0,0,0,.3); }
  .photo-frame .photo { position: absolute; left: 16px; top: 16px; width: 178px; height: 178px; }
  .photo-frame--1 { top: 192px; } .photo-frame--1 .photo { background: linear-gradient(180deg, #bfe3ea 0%, #c9b8a8 45%, #8c3f45 60%, #d8d6d2 100%); }
  .photo-frame--2 { top: 419px; } .photo-frame--2 .photo { background: linear-gradient(180deg, #b9c3c8 0%, #8a9499 45%, #2c3134 70%, #1d2124 100%); }
  .photo-frame--3 { top: 646px; } .photo-frame--3 .photo { background: linear-gradient(180deg, #5d7d97 0%, #c9d2d8 35%, #d83a3a 58%, #2f4a66 80%, #1f3550 100%); }
  .photo-frame--4 { top: 873px; } .photo-frame--4 .photo { background: linear-gradient(135deg, #4fb29a 0%, #6dc4ad 45%, #b3502e 75%, #cfcfcf 100%); }

  /* Services */
  .services-tag { position: absolute; left: 122px; top: 529px; width: 424px; height: 64px; }
  .services-tag svg { position: absolute; inset: 0; }
  .services-tag h2 { position: absolute; left: 0; right: 0; top: 8px; text-align: center; font-family: "Montserrat", Arial, sans-serif; font-style: italic; font-weight: 800; font-size: 38px; letter-spacing: -1.5px; color: var(--ink); line-height: 48px; }

  .service-list { position: absolute; left: 36px; top: 635px; list-style: none; }
  .service-list li { display: flex; align-items: center; height: 50.8px; font-style: italic; font-weight: 400; font-size: 20.5px; color: var(--ink); text-transform: uppercase; }
  .service-list li::before { content: ""; width: 25px; height: 25px; border: 4px solid var(--orange); margin-right: 19px; flex: none; }

  /* Footer */
  .footer { position: absolute; left: 0; top: 1109px; width: 927px; height: 91px; background: var(--orange); }
  .footer-line { position: absolute; left: 326px; display: flex; align-items: center; gap: 16px; font-style: italic; font-size: 19px; color: var(--white); }
  .footer-line--address { top: 14px; }
  .footer-line--web { top: 51px; }
  .footer-line svg { width: 24px; height: 26px; flex: none; }
</style>
</head>
<body>
<div class="flyer">

  <header>
    <div class="brand">
      <div class="brand-mark"></div>
      <div class="brand-name">Brightwater Haulage Global</div>
    </div>

    <div class="contact-phone">
      <svg width="40" height="40" viewBox="0 0 40 40" fill="none" stroke="#fff" stroke-width="2.4" stroke-linecap="round" stroke-linejoin="round">
        <circle cx="20" cy="20" r="17"/>
        <path d="M13 11.5l3.5-1 2.5 5-2.2 1.6c1 2.4 2.8 4.3 5.2 5.3l1.6-2.2 5 2.5-1 3.5c-.4 1-1.4 1.5-2.4 1.3-6.2-1.3-11-6.1-12.3-12.3-.2-1 .3-2 1.1-2.7z"/>
        <path d="M23 11.5a6 6 0 0 1 5 5M23.5 7.8a9.5 9.5 0 0 1 8.2 8.2"/>
      </svg>
    </div>
    <div class="phone-numbers">
      <div>+123-456-789</div>
      <div>+123-456-789</div>
    </div>
  </header>

  <section class="hero">
    <div class="hero-map" role="img" aria-label="Dark silhouette world map spanning the banner"></div>
    <h1 class="hero-title">We<br>are provide<br>our best service</h1>
  </section>

  <aside>
    <div class="photo-frame photo-frame--1"><div class="photo" role="img" aria-label="Stacked shipping containers at a port with a plane flying overhead at sunset"></div></div>
    <div class="photo-frame photo-frame--2"><div class="photo" role="img" aria-label="Truck trailer driving along a highway"></div></div>
    <div class="photo-frame photo-frame--3"><div class="photo" role="img" aria-label="Red cargo ship sailing under a cloudy sky"></div></div>
    <div class="photo-frame photo-frame--4"><div class="photo" role="img" aria-label="Courier wheeling boxes on a hand truck past a shopfront"></div></div>
  </aside>

  <section class="services">
    <div class="services-tag">
      <svg width="424" height="64" viewBox="0 0 424 64">
        <polygon points="38,0 424,0 386,64 0,64" fill="var(--orange)"/>
        <polygon points="0,64 386,64 384,67 0,67" fill="rgba(0,0,0,.35)"/>
      </svg>
      <h2>OUR SERVICES</h2>
    </div>

    <ul class="service-list">
      <li>Ocean/Air Import and Export</li>
      <li>Exhibition Cargo</li>
      <li>Carnet&nbsp; Application</li>
      <li>Project Cargo (OOG/Flatrack/Reefer/DG)</li>
      <li>Customs Clearance</li>
      <li>Door to Door Services</li>
      <li>Cargo Insurance</li>
      <li>Warehousing</li>
      <li>Trucking (LTL/FCL)</li>
    </ul>
  </section>

  <footer class="footer">
    <div class="footer-line footer-line--address">
      <svg viewBox="0 0 24 26"><path d="M12 1a8 8 0 0 0-8 8c0 6 8 16 8 16s8-10 8-16a8 8 0 0 0-8-8zm0 11a3.2 3.2 0 1 1 0-6.4 3.2 3.2 0 0 1 0 6.4z" fill="#fff"/></svg>
      <span>123 YOUR STREET ADDRESS</span>
    </div>
    <div class="footer-line footer-line--web">
      <svg viewBox="0 0 24 26" fill="none" stroke="#fff" stroke-width="1.6"><circle cx="12" cy="13" r="10.5"/><ellipse cx="12" cy="13" rx="4.5" ry="10.5"/><path d="M1.5 13h21M3.5 7.5h17M3.5 18.5h17"/></svg>
      <span>WWW.YOUR-WEBSITE.COM</span>
    </div>
  </footer>

</div>
</body>
</html>
```